Poster Design Needed for Events

I would like a poster designed for our events.. We do evenings of Mediumship/Psychic at theatres ect.. the image below would need to be included... I Would also like the following wording to be included... "Renowned Spiritualist Medium Dafydd Pemberton Presents Whispers From the Lighthouse" There will also Need to be a Place on the poster where event details can be put.. as they Change everytime.. Colours for background maybe blue,, maybe Clouds ect..

```html
<!DOCTYPE html>
<html lang="en">
<head>
<meta charset="utf-8">
<title>Whispers From the Lighthouse – Event Poster</title>
<link rel="stylesheet" href="https://fonts.googleapis.com/css2?family=Cinzel:wght@700&family=Josefin+Sans:wght@400;700&family=Lobster&display=swap">
<style>
  :root {
    --sky-top: #eef4fa;
    --sky-mid: #a9cbe9;
    --sky-low: #7fb0df;
    --sky-bottom: #6295cf;
    --ink-blue: #2a5b9f;
    --ink-soft: #3d6ba8;
    --rule-blue: #6d9bd3;
    --suit-navy: #1a2747;
    --suit-mid: #34477a;
    --white: #ffffff;
  }
  html, body {
    margin: 0;
    padding: 0;
    width: 906px;
    height: 1200px;
    overflow: hidden;
    background: var(--sky-top);
  }
  .poster {
    position: relative;
    width: 906px;
    height: 1200px;
    overflow: hidden;
  }
  .sky-backdrop {
    position: absolute;
    inset: 0;
    background:
      radial-gradient(ellipse 60% 30% at 50% 22%, rgba(255,255,255,0.85), rgba(255,255,255,0) 70%),
      linear-gradient(180deg, var(--sky-top) 0%, var(--sky-mid) 38%, var(--sky-low) 65%, var(--sky-bottom) 100%);
  }
  .presenter-photo {
    position: absolute;
    left: 0;
    top: 427px;
    width: 468px;
    height: 773px;
    border-radius: 200px 200px 0 0;
    background: linear-gradient(180deg, rgba(52,71,122,0.55) 0%, var(--suit-mid) 35%, var(--suit-navy) 100%);
  }
  .headline {
    position: absolute;
    left: 0;
    top: 0;
    width: 906px;
    height: 340px;
  }
  .headline .title-caps {
    font-family: "Cinzel", "Times New Roman", serif;
    font-weight: 700;
    fill: var(--ink-blue);
  }
  .headline .title-script {
    font-family: "Lobster", "Brush Script MT", cursive;
    fill: var(--ink-blue);
  }
  .headline .rule {
    stroke: var(--rule-blue);
    stroke-width: 1.2;
  }
  .headline .dotted-rule {
    stroke: var(--ink-soft);
    stroke-width: 2;
    stroke-dasharray: 2 5;
  }
  .presenter-credit {
    position: absolute;
    left: 0;
    top: 338px;
    width: 906px;
    text-align: center;
    font-family: "Josefin Sans", Arial, sans-serif;
    font-size: 29px;
    line-height: 33px;
    letter-spacing: 1px;
    color: var(--ink-soft);
    text-transform: uppercase;
    margin: 0;
  }
  .presenter-credit .presenter-name {
    font-weight: 700;
    color: var(--ink-blue);
  }
  .event-details {
    position: absolute;
    right: 84px;
    top: 762px;
    width: 260px;
    text-align: right;
  }
  .event-details .invite {
    font-family: "Lobster", "Brush Script MT", cursive;
    font-size: 56px;
    line-height: 64px;
    color: var(--white);
    margin: 0 0 6px 0;
  }
  .event-details .date-box {
    display: inline-block;
    width: 240px;
    height: 76px;
    line-height: 84px;
    text-align: center;
    background: var(--ink-blue);
    color: var(--white);
    font-family: "Josefin Sans", Arial, sans-serif;
    font-weight: 700;
    font-size: 38px;
    letter-spacing: 1px;
  }
  .event-details .year {
    display: block;
    width: 240px;
    margin-left: auto;
    text-align: center;
    font-family: "Josefin Sans", Arial, sans-serif;
    font-weight: 700;
    font-size: 82px;
    line-height: 96px;
    color: var(--white);
    letter-spacing: 2px;
  }
</style>
</head>
<body>
  <main class="poster">
    <div class="sky-backdrop" role="img" aria-label="Photograph of a bright blue sky with white clouds and sunbeams breaking through"></div>

    <svg class="headline" viewBox="0 0 906 340" width="906" height="340" aria-label="Whispers From the Lighthouse">
      <text class="title-caps" x="453" y="113" text-anchor="middle" font-size="68" textLength="720" lengthAdjust="spacingAndGlyphs">Whispers From</text>
      <line class="rule" x1="104" y1="156" x2="380" y2="156"/>
      <line class="rule" x1="104" y1="162" x2="380" y2="162"/>
      <line class="rule" x1="540" y1="156" x2="815" y2="156"/>
      <line class="rule" x1="540" y1="162" x2="815" y2="162"/>
      <text class="title-script" x="460" y="180" text-anchor="middle" font-size="60">the</text>
      <text class="title-caps" x="463" y="296" text-anchor="middle" font-size="100" textLength="718" lengthAdjust="spacingAndGlyphs">LIGHTHOUSE</text>
      <line class="dotted-rule" x1="243" y1="325" x2="688" y2="325"/>
    </svg>

    <p class="presenter-credit">
      Renowned Spiritualist Medium<br>
      <span class="presenter-name">Dafydd Pemberton</span> Presents
    </p>

    <div class="presenter-photo" role="img" aria-label="Photograph of the medium in a dark suit and white shirt, reaching out a welcoming hand"></div>

    <section class="event-details">
      <p class="invite">Join us on</p>
      <span class="date-box">1ST JAN</span>
      <span class="year">2016</span>
    </section>
  </main>
</body>
</html>
```